Luggage and travel essentials company needs Letterhead design (including logo)

Brenmoor luggage is a travel retailer focussed on selling luggage and travel essentials.
We are a company that have a traditional approach to customer service and also embraces the latest technology, especially where it improves the customer experience.
I would like the design to have an airport hint (airport imagery and font preferred), I would also like the colour blue to feature heavily (see attached image for colour hint).
The final design should aim to give the customer confidence that we are dependable and reliable (no script fonts or crazy colours please) but also reflect that we are an innovative and technology focused company.
I would like the letterhead design to include a logo and text.
I am interested in letterhead text containing an embedded logo (much like the 'A' in Zyvanta's logo is also used separately) Note: this is optional.
The text of the letterhead should include the words "Brenmoor Luggage & Travel Essentials", and should include a space for the company phone number, email address, website address along with the company physical address.
Target Market(s)
Affluent Adults aged 25 years and above - Predominantly female
Industry/Entity Type
Airport

```html
<!DOCTYPE html>
<html lang="en">
<head>
<meta charset="utf-8">
<title>Brenmoor Luggage &amp; Travel Essentials – Letterhead</title>
<link rel="stylesheet" href="https://fonts.googleapis.com/css2?family=Questrial&display=swap">
<style>
  :root {
    --backdrop: #ececec;
    --paper: #ffffff;
    --teal: #0e7f92;
    --sky: #35a3cc;
    --ink: #5a5f63;
    --icon-ring: #8fc6d8;
  }
  * { box-sizing: border-box; margin: 0; padding: 0; }
  html, body {
    width: 1200px; height: 936px; overflow: hidden;
    background: var(--backdrop);
    font-family: "Questrial", "Century Gothic", sans-serif;
  }
  .letterhead {
    position: absolute; left: 289px; top: 28px;
    width: 622px; height: 880px;
    background: var(--paper);
    box-shadow: 0 2px 10px rgba(0,0,0,0.12);
  }
  .top-band {
    position: absolute; top: 0; height: 8px;
  }
  .top-band--primary { left: 0; width: 402px; background: var(--teal); }
  .top-band--accent { left: 410px; right: 0; background: var(--sky); }

  .brand {
    position: absolute; left: 40px; top: 56px;
    display: flex; align-items: center; gap: 12px;
  }
  .brand-dot {
    width: 46px; height: 46px; border-radius: 50%;
    background: var(--teal); flex: none;
  }
  .brand-name {
    color: var(--teal); font-size: 17px; line-height: 1.2;
    letter-spacing: 0.3px;
  }

  .contact {
    position: absolute; left: 420px; top: 40px;
    list-style: none; color: var(--ink);
    font-size: 8.5px; line-height: 1;
  }
  .contact li {
    display: flex; align-items: center; gap: 6px; margin-bottom: 5px;
  }
  .contact svg { width: 10px; height: 10px; flex: none; }
  .contact .address { padding-left: 16px; line-height: 1.35; margin-top: 2px; }
</style>
</head>
<body>
  <main class="letterhead">
    <div class="top-band top-band--primary"></div>
    <div class="top-band top-band--accent"></div>

    <header class="brand">
      <span class="brand-dot"></span>
      <p class="brand-name">Brenmoor<br>Luggage &amp;<br>Travel Essentials</p>
    </header>

    <ul class="contact">
      <li>
        <svg viewBox="0 0 10 10"><circle cx="5" cy="5" r="4.5" fill="none" stroke="var(--icon-ring)"/><path d="M3.3 2.8c.4 1.9 1.6 3.3 3.5 4l.5-.9-1-.6-.5.5c-.8-.4-1.3-1-1.6-1.7l.5-.5-.6-1z" fill="var(--sky)"/></svg>
        (03) 9410 5527
      </li>
      <li>
        <svg viewBox="0 0 10 10"><circle cx="5" cy="5" r="4.5" fill="none" stroke="var(--icon-ring)"/><rect x="3" y="3.2" width="4" height="3.6" fill="var(--sky)"/></svg>
        (03) 9410 5528
      </li>
      <li>
        <svg viewBox="0 0 10 10"><circle cx="5" cy="5" r="4.5" fill="none" stroke="var(--icon-ring)"/><rect x="2.8" y="3.3" width="4.4" height="3.2" fill="none" stroke="var(--sky)" stroke-width="0.8"/><path d="M2.8 3.3 5 5l2.2-1.7" fill="none" stroke="var(--sky)" stroke-width="0.8"/></svg>
        info@brenmoorluggage.com
      </li>
      <li>
        <svg viewBox="0 0 10 10"><circle cx="5" cy="5" r="4.5" fill="none" stroke="var(--icon-ring)"/><circle cx="5" cy="5" r="2.3" fill="none" stroke="var(--sky)" stroke-width="0.8"/><path d="M2.7 5h4.6M5 2.7v4.6" stroke="var(--sky)" stroke-width="0.6"/></svg>
        www.brenmoorluggage.com
      </li>
      <li class="address">1420 Harrow Lane<br>Ashford, IA 50199</li>
    </ul>
  </main>
</body>
</html>
```